New Alcoholic Spiked Seltzer Line

We need a can design for a line of low calorie alcoholic seltzer. This product is a sparkling water and vodka drink with no sugar added in a slim 12 oz can.

This is a lighter, healthier, alternative to the sugary ready-to-drinks on the market. The product contains only 3 ingredients: Vodka, Water and Natural Flavors. It has only 100 calories but still has 5% alcohol, so you don't need to sacrifice alcohol to cut calories.

This product also does not contain any preservatives.

We want this design to communicate the following objectives to the consumer and in this order:

1. Appetizing product
2.Low calorie
3.Communicate the type of beverage (Spiked Seltzer)

The brand name of the product is VELKA.

The flavor of the product needed to be used for the design is Mango-Orange.

Comparable products are:

www.brisavelfizz.example/
https://www.tarnowbubble.example
https://quellrind.example/

The designs should not infringe or copy the creative directions of the products mentionned above. They are only given so that you can better understand the type of product we are developing.

Target Market(s)

Young Professional women between the ages of 25 and 44

Industry/Entity Type

Product

Colors

Designer to choose colors to be used in the design.

Requirements
Must have
• Design extendibility, meaning it can be adapted for other flavors.
• This is a new category in the market we are targeting, so consumers must easily be able to identify what type of product this is.

```html
<!DOCTYPE html>
<html lang="en">
<head>
<meta charset="utf-8">
<title>VELKA Spiked Seltzer – Mango-Orange can label</title>
<link rel="stylesheet" href="https://fonts.googleapis.com/css2?family=Italiana&family=Josefin+Sans:wght@400;600&display=swap">
<style>
  :root {
    --backdrop: #ececec;
    --band-light: #f6c232;
    --band-deep: #eea21c;
    --orange: #f08a1f;
    --orange-deep: #e8562a;
    --red: #e03a2c;
    --gold: #f6b62e;
    --white: #ffffff;
    --pill-text: #ee8a1e;
  }
  html, body {
    margin: 0;
    width: 1200px;
    height: 953px;
    overflow: hidden;
    background: var(--backdrop);
  }
  .can-label {
    position: absolute;
    left: 390px;
    top: 40px;
    width: 420px;
    height: 873px;
    overflow: hidden;
    background: var(--orange);
  }
  .label-band {
    position: absolute;
    left: 0;
    width: 100%;
    height: 48px;
    background: linear-gradient(90deg, var(--band-deep), var(--band-light) 45%, var(--band-deep));
  }
  .label-band--top { top: 0; }
  .label-band--bottom { bottom: 0; }
  .wave-artwork {
    position: absolute;
    left: 0;
    top: 48px;
    width: 100%;
    height: 777px;
    background:
      radial-gradient(ellipse 70% 30% at 70% 45%, rgba(224,58,44,.75), transparent 70%),
      radial-gradient(ellipse 60% 25% at 25% 60%, rgba(232,86,42,.6), transparent 70%),
      radial-gradient(ellipse 80% 30% at 50% 85%, rgba(246,182,46,.9), transparent 70%),
      linear-gradient(180deg, var(--gold) 0%, var(--orange) 30%, var(--orange-deep) 55%, var(--orange) 75%, var(--gold) 100%);
  }
  .label-arcs {
    position: absolute;
    inset: 0;
  }
  .arc-text {
    font-family: "Josefin Sans", sans-serif;
    font-size: 17px;
    letter-spacing: 4px;
    fill: var(--white);
    text-transform: uppercase;
  }
  .brand-name {
    position: absolute;
    top: 208px;
    left: 0;
    width: 100%;
    margin: 0;
    text-align: center;
    font-family: "Italiana", serif;
    font-weight: 400;
    font-size: 118px;
    line-height: 1;
    color: var(--white);
  }
  .product-type {
    position: absolute;
    top: 348px;
    left: 0;
    width: 100%;
    margin: 0;
    text-align: center;
    font-family: "Italiana", serif;
    font-weight: 400;
    color: var(--white);
    line-height: 1;
  }
  .product-type span { display: block; }
  .product-type .word-spiked { font-size: 78px; }
  .product-type .word-seltzer { font-size: 70px; margin-top: 4px; margin-left: 50px; }
  .nutrition-claims {
    position: absolute;
    top: 660px;
    left: 0;
    width: 100%;
    margin: 0;
    text-align: center;
    font-family: "Josefin Sans", sans-serif;
    font-size: 22px;
    line-height: 30px;
    color: var(--white);
  }
  .flavour-pill {
    position: absolute;
    top: 738px;
    left: 100px;
    width: 220px;
    height: 38px;
    border-radius: 19px;
    background: var(--white);
    color: var(--pill-text);
    font-family: "Josefin Sans", sans-serif;
    font-size: 20px;
    line-height: 41px;
    text-align: center;
  }
</style>
</head>
<body>
  <main class="can-label">
    <div class="label-band label-band--top"></div>
    <div class="wave-artwork" role="img" aria-label="Flowing mango, orange and red line-wave pattern"></div>

    <svg class="label-arcs" width="420" height="873" viewBox="0 0 420 873">
      <defs>
        <path id="arc-tagline" d="M 80 250 Q 210 150 340 250"/>
        <path id="arc-claim" d="M 4 560 Q 210 760 416 560"/>
      </defs>
      <text class="arc-text"><textPath href="#arc-tagline" startOffset="50%" text-anchor="middle">The New Cool</textPath></text>
      <text class="arc-text"><textPath href="#arc-claim" startOffset="50%" text-anchor="middle">Enriched with Natural Flavours</textPath></text>
    </svg>

    <h1 class="brand-name">VELKA</h1>
    <h2 class="product-type"><span class="word-spiked">Spiked</span><span class="word-seltzer">Seltzer</span></h2>
    <p class="nutrition-claims">ONLY 100 CALORIES<br>5% ALC/VOL</p>
    <div class="flavour-pill">MANGO-ORANGE</div>

    <div class="label-band label-band--bottom"></div>
  </main>
</body>
</html>
```